Flyer Design Project

I require a double sided flyer in PSD format.
The flyer should look fresh and clean.
The flyer is for an digital marketing company that offers various services. The services are broken down into 3 main categories and the design should reflect this.
All the content is provided in the attached file
Industry/Entity Type
Digital
Requirements
Must have
- Front of the leaflet to be mainly white background with appealing text based questions in the colours in large font with relevant images.
Back if the
3 separate boxes using the colours indicated in the attachment for the services on back of the leafet.
Should not have
- Gradients
Borders on the edges of the design
Vignettes
Black elements
Any text below 10pt
Fancy fonts
Do not use old-style fonts

```html
<!DOCTYPE html>
<html lang="en">
<head>
<meta charset="utf-8">
<title>Digital Marketing Flyer – Front and Back</title>
<link rel="stylesheet" href="https://fonts.googleapis.com/css2?family=Montserrat:wght@700;800&family=Quicksand:wght@400;500;700&display=swap">
<style>
  :root{
    --green:#8dc63f;
    --green-dark:#10994a;
    --blue:#3cc0e2;
    --blue-dark:#1f6db8;
    --orange:#f47f20;
    --orange-dark:#e0692a;
    --white:#ffffff;
    --canvas:#eeeeee;
    --body-font:"Quicksand", "Nunito", sans-serif;
    --display-font:"Montserrat", "Arial", sans-serif;
  }
  *{box-sizing:border-box;margin:0;padding:0}
  html,body{width:1200px;height:1000px;overflow:hidden}
  body{background:var(--canvas);font-family:var(--body-font);position:relative}

  .flyer{position:absolute;top:80px;width:560px;height:840px;background:var(--white);overflow:hidden;box-shadow:0 2px 10px rgba(0,0,0,.12)}
  .flyer--services{left:20px}
  .flyer--questions{left:620px}
  .flyer__bg{position:absolute;left:0;top:0}

  /* ---------- services side ---------- */
  .service-list{position:absolute;left:32px;list-style:none;color:var(--white);font-size:23px;font-weight:500;line-height:28px;white-space:nowrap}
  .service-list li::before{content:"•";margin-right:10px}
  .service-list b{font-weight:700}
  .service-list--consulting{top:16px}
  .service-list--design{top:224px}
  .service-list--sem{top:428px}

  .offer{position:absolute;left:42px;width:412px;border:2px dashed var(--white);color:var(--white);text-align:center;font-weight:700;line-height:1.05}
  .offer--consulting{top:128px;height:64px;background:var(--green-dark);font-size:23px;padding-top:6px}
  .offer--design{top:344px;height:60px;background:var(--blue-dark);font-size:23px;padding-top:4px}
  .offer--sem{top:664px;height:62px;background:var(--orange-dark);font-size:22px;padding-top:6px}
  .offer--sem small{font-size:19px;display:block}
  .offer .accent{color:var(--orange)}

  .category-label{position:absolute;left:488px;width:44px;writing-mode:vertical-rl;color:var(--orange);font-size:17px;line-height:20px;text-transform:uppercase;white-space:nowrap}
  .category-label b{font-weight:700}
  .category-label--consulting{top:30px}
  .category-label--design{top:262px}
  .category-label--sem{top:530px}

  .services-footer{position:absolute;left:34px;top:768px;color:var(--orange);font-weight:700;font-size:15px;line-height:22px}
  .services-footer .call{font-weight:500;font-size:17px}
  .services-footer .call b{font-weight:700}
  .services-footer svg{vertical-align:-2px;margin-right:4px}

  .logo-slot{position:absolute;background:var(--blue);color:var(--white);text-align:center;font-weight:700;line-height:1}
  .logo-slot span{font-weight:400;display:block}
  .logo-slot--services{left:440px;top:770px;width:100px;height:34px;font-size:13px;padding-top:4px}
  .logo-slot--questions{left:50px;top:688px;width:236px;height:90px;font-size:32px;padding-top:14px}

  /* ---------- questions side ---------- */
  .q{position:absolute;left:56px;text-transform:uppercase;color:var(--green);font-weight:500;white-space:nowrap}
  .q b{font-weight:700;color:var(--orange)}
  .q-know{top:40px;font-size:28px;line-height:34px}
  .q-stat{top:74px;left:50px;font-family:var(--display-font);font-weight:800;font-size:108px;color:var(--orange);letter-spacing:-4px;line-height:1}
  .q-stat sup{font-size:28px;letter-spacing:0;vertical-align:-6px}
  .q-arrow{position:absolute;left:236px;top:74px}
  .q-fact{top:192px;font-size:27px;line-height:32px}
  .q-online{top:290px;font-size:30px;line-height:32px}
  .q-need{top:392px;font-size:30px;line-height:34px;letter-spacing:15px}
  .q-more{top:424px;left:46px;font-family:var(--display-font);font-weight:800;font-size:112px;line-height:1}
  .q-customers{top:540px;font-size:48px;line-height:1}
  .q-customers.q{color:var(--orange)}
  .q-business{top:592px;font-size:28px;line-height:32px}
  .divider{position:absolute;left:56px;width:470px;border-top:2px dashed var(--orange)}
  .divider--1{top:268px}
  .divider--2{top:372px}
  .divider--3{top:638px}
  .tagline{position:absolute;left:50px;top:652px;color:var(--orange);font-weight:700;font-size:17px;white-space:nowrap}
  .questions-call{position:absolute;left:16px;top:806px;color:var(--white);font-size:18px;font-weight:500;white-space:nowrap}
  .questions-call b{font-weight:700}
</style>
</head>
<body>

<section class="flyer flyer--services" aria-label="Services side">
  <svg class="flyer__bg" width="560" height="840" viewBox="0 0 560 840" aria-hidden="true">
    <path fill="#8dc63f" d="M0 0 H500 C470 60 470 160 560 215 H0 Z"/>
    <path fill="#3cc0e2" d="M0 215 H560 C470 260 470 370 560 415 H0 Z"/>
    <path fill="#f47f20" d="M0 415 H560 C460 480 460 680 560 745 H0 Z"/>
  </svg>

  <ul class="service-list service-list--consulting">
    <li>Marketing <b>strategy</b> and <b>planning</b></li>
    <li>Business <b>branding</b></li>
    <li>Competition <b>analysis</b>,</li>
  </ul>
  <div class="offer offer--consulting">GET<br><span class="accent">FREE</span> CONSULTATION</div>
  <div class="category-label category-label--consulting"><b>Consulting</b><br>Services</div>

  <ul class="service-list service-list--design">
    <li>Web Design</li>
    <li>Website maintenance</li>
    <li>Logo design</li>
    <li>Flyer design</li>
  </ul>
  <div class="offer offer--design">GET<br><span class="accent">FREE</span> WEBSITE</div>
  <div class="category-label category-label--design"><b>Design</b><br>Services</div>

  <ul class="service-list service-list--sem">
    <li>Local Business Marketing</li>
    <li>PPC</li>
    <li>Email marketing</li>
    <li>SEO</li>
    <li>Social media</li>
    <li>Content development</li>
    <li>Website audit</li>
    <li>Lead generation</li>
  </ul>
  <div class="offer offer--sem">25% OFF<small>any SEM Package</small></div>
  <div class="category-label category-label--sem"><b>SEM</b><br>Services</div>

  <div class="services-footer">
    <div><svg width="11" height="15" viewBox="0 0 11 15" aria-hidden="true"><path fill="#f47f20" d="M5.5 0A5.5 5.5 0 0 0 0 5.5C0 9.5 5.5 15 5.5 15S11 9.5 11 5.5A5.5 5.5 0 0 0 5.5 0Zm0 7.6a2.1 2.1 0 1 1 0-4.2 2.1 2.1 0 0 1 0 4.2Z"/></svg>Kestrel House, 12 Canal Walk, Birmingham, B1 9ZZ</div>
    <div class="call">Call <b>0121 555 0148</b> for a <b>FREE</b></div>
  </div>
  <div class="logo-slot logo-slot--services">LOGO<span>HERE</span></div>
</section>

<section class="flyer flyer--questions" aria-label="Questions side">
  <svg class="flyer__bg" width="560" height="840" viewBox="0 0 560 840" aria-hidden="true">
    <path fill="#3cc0e2" d="M0 790 C120 745 330 755 430 790 C480 808 530 808 560 798 V840 H0 Z"/>
  </svg>

  <div class="q q-know">Did you know</div>
  <div class="q-stat" style="position:absolute">85<sup>%</sup></div>
  <svg class="q-arrow" width="40" height="100" viewBox="0 0 40 100" aria-hidden="true">
    <path d="M20 0 V96 M5 76 L20 98 L35 76" fill="none" stroke="#8dc63f" stroke-width="3"/>
  </svg>
  <div class="q q-fact">Of consumers use the internet<br>to find <b>business</b> like yours ?</div>
  <div class="divider divider--1"></div>

  <div class="q q-online">Are your customers<br><b>finding you</b> online ?</div>
  <div class="divider divider--2"></div>

  <div class="q q-need">Do you need</div>
  <div class="q q-more">More</div>
  <div class="q q-customers">Customers</div>
  <div class="q q-business">For your business ?</div>
  <div class="divider divider--3"></div>

  <div class="tagline">Let us help you grow your business online</div>
  <div class="logo-slot logo-slot--questions">LOGO<span>HERE</span></div>

  <div class="questions-call">Call <b>0121 555 0148</b> for a <b>FREE</b></div>
</section>

</body>
</html>
```